Flyer for a marketing

We are a holistic mental health facility in need of a flyer to help promote our services and encourage more people to seek care. See the attachment to tell you more. We prefer warm green colors or rich blue. Thank you.

```html
<!DOCTYPE html>
<html lang="en">
<head>
<meta charset="utf-8">
<title>Evergreen Mind Health and Wellness – Flyer</title>
<link href="https://fonts.googleapis.com/css2?family=Montserrat:wght@400&family=Source+Sans+3:wght@300;400;600;700&family=Ubuntu:wght@700&display=swap" rel="stylesheet">
<style>
  :root {
    --page-bg: #ece9e4;
    --paper: #f5f6f5;
    --navy: #1f3164;
    --navy-text: #1d3a6e;
    --sky: #2fc0ec;
    --green: #2e7a3f;
    --green-dark: #1f5d2c;
    --lime: #a3cc37;
    --grey-text: #555a5e;
    --ink: #1e1e1e;
    --white: #ffffff;
  }
  * { box-sizing: border-box; margin: 0; padding: 0; }
  html, body { width: 1066px; height: 1200px; overflow: hidden; }
  body { background: var(--page-bg); font-family: "Source Sans 3", sans-serif; position: relative; }

  .flyer {
    position: absolute; left: 87px; top: 23px;
    width: 892px; height: 1153px;
    background: var(--paper);
    overflow: hidden;
  }

  /* header */
  .masthead { position: absolute; left: 0; top: 0; width: 100%; height: 307px; }
  .brand {
    position: absolute; left: 0; width: 100%; top: 68px;
    display: flex; justify-content: center; align-items: center; gap: 18px;
  }
  .brand-mark { width: 26px; height: 26px; border-radius: 50%; background: var(--sky); }
  .brand-name {
    font-family: "Source Sans 3", sans-serif; font-weight: 700;
    font-size: 30px; line-height: 32px; color: var(--navy-text);
  }
  .tagline {
    position: absolute; top: 236px; width: 100%; text-align: center;
    font-family: "Montserrat", sans-serif; font-size: 28px; letter-spacing: 1px;
    color: var(--navy-text);
  }

  /* photo strip */
  .photo-band { position: absolute; top: 307px; left: 0; width: 100%; height: 283px; background: var(--navy); }
  .photo { position: absolute; top: 23px; height: 195px; }
  .photo--telehealth { left: 0; width: 292px; background: linear-gradient(135deg, #8a8f8c, #3f4a4f 60%, #2a3438); }
  .photo--consult { left: 299px; width: 293px; background: linear-gradient(135deg, #f2f1ef, #d9d6d2 60%, #9c8f86); }
  .photo--session { left: 600px; width: 292px; background: linear-gradient(135deg, #e9eaec, #b9bcc2 55%, #6d7079); }
  .url-tab {
    position: absolute; left: 228px; top: 233px; width: 436px; height: 50px;
  }
  .url-tab svg { position: absolute; inset: 0; }
  .url-tab span {
    position: absolute; width: 100%; top: 8px; text-align: center;
    font-weight: 700; font-size: 27px; color: var(--ink);
  }

  /* green banner */
  .hero { position: absolute; top: 590px; left: 0; width: 100%; height: 202px; background: var(--green); }
  .hero-leaf {
    position: absolute; left: 0; top: 0; width: 200px; height: 202px;
    background: radial-gradient(ellipse at 40% 45%, #8fbf3e 0%, #5b9a33 45%, rgba(46,122,63,0) 80%);
  }
  .hero-title {
    position: absolute; left: 103px; top: 10px;
    font-weight: 700; font-size: 45px; letter-spacing: -0.5px; color: var(--white);
    text-shadow: 0 2px 2px rgba(0,0,0,0.35);
  }
  .hero-sub {
    position: absolute; left: 105px; top: 66px;
    font-weight: 700; font-size: 27px; color: var(--white);
    text-shadow: 0 2px 2px rgba(0,0,0,0.35);
  }
  .hero-rule {
    position: absolute; left: 170px; top: 122px; width: 658px; height: 2px;
    background: linear-gradient(90deg, var(--lime) 0%, var(--lime) 45%, var(--sky) 45%, var(--sky) 100%);
  }
  .hero-note {
    position: absolute; left: 158px; top: 138px;
    font-weight: 400; font-size: 31px; color: var(--white);
  }

  /* lower content */
  .contact { position: absolute; left: 28px; top: 812px; width: 352px; text-align: center; }
  .contact-lead { font-weight: 300; font-size: 23px; line-height: 28px; color: var(--grey-text); }
  .contact-label { margin-top: 36px; font-weight: 600; font-size: 21px; color: var(--grey-text); }
  .contact-phone { font-weight: 700; font-size: 38px; line-height: 42px; color: var(--green); }
  .contact-email { margin-top: 8px; font-weight: 600; font-size: 19px; color: var(--grey-text); }
  .contact-rule {
    margin: 12px auto 0; width: 324px; height: 2px;
    background: linear-gradient(90deg, var(--lime), var(--sky));
  }
  .contact-address { margin-top: 12px; font-size: 14.5px; line-height: 19px; color: var(--ink); }
  .contact-address b { font-weight: 700; }

  .divider {
    position: absolute; left: 406px; top: 812px; width: 2px; height: 275px;
    background: linear-gradient(180deg, rgba(0,0,0,0.05), rgba(0,0,0,0.22) 50%, rgba(0,0,0,0.05));
  }

  .benefits { position: absolute; left: 450px; top: 812px; width: 420px; }
  .benefits-title {
    font-family: "Ubuntu", sans-serif; font-weight: 700;
    font-size: 27px; line-height: 32px; color: var(--sky);
  }
  .benefits-sub { margin-top: 18px; font-weight: 700; font-size: 20px; color: #333; }
  .benefits-list { list-style: none; margin-top: 12px; }
  .benefits-list li {
    position: relative; padding-left: 22px; margin-bottom: 8px;
    font-size: 16px; line-height: 19px; color: #444;
  }
  .benefits-list li::before {
    content: ""; position: absolute; left: 0; top: 4px;
    width: 13px; height: 11px; border-radius: 50%;
    background: radial-gradient(circle at 35% 35%, #b5e061, #4ea528);
  }

  .footer {
    position: absolute; left: 0; bottom: 0; width: 100%; height: 40px;
    background: var(--sky); text-align: center;
    font-weight: 700; font-size: 13.5px; line-height: 40px; color: #274060;
  }
</style>
</head>
<body>
  <main class="flyer">
    <header class="masthead">
      <div class="brand">
        <span class="brand-mark"></span>
        <div class="brand-name">Evergreen<br>Mind<br>Health<br>and<br>Wellness</div>
      </div>
      <p class="tagline">The Care You Deserve</p>
    </header>

    <section class="photo-band">
      <div class="photo photo--telehealth" role="img" aria-label="Photo of a patient holding a pill bottle during a video call with a doctor"></div>
      <div class="photo photo--consult" role="img" aria-label="Photo of a doctor in a white coat consulting with a patient at a desk"></div>
      <div class="photo photo--session" role="img" aria-label="Photo of a young girl on a sofa talking with a counselor"></div>
      <div class="url-tab">
        <svg width="436" height="50" viewBox="0 0 436 50" aria-hidden="true">
          <defs>
            <linearGradient id="tabFill" x1="0" y1="0" x2="0" y2="1">
              <stop offset="0" stop-color="#b6d93f"/>
              <stop offset="1" stop-color="#7fb431"/>
            </linearGradient>
          </defs>
          <path d="M0 50 C18 50 22 0 50 0 H386 C414 0 418 50 436 50 Z" fill="url(#tabFill)"/>
        </svg>
        <span>evergreenmindhealth.com</span>
      </div>
    </section>

    <section class="hero">
      <div class="hero-leaf" role="img" aria-label="Image of a green sage leaf with a yellow herbal capsule"></div>
      <h1 class="hero-title">Evergreen Mind Health and Wellness,</h1>
      <p class="hero-sub">where deserving patients meet compassionate providers.</p>
      <div class="hero-rule"></div>
      <p class="hero-note">We are accepting new patients, no waiting list.</p>
    </section>

    <section class="contact">
      <p class="contact-lead">Your mental health matters, so<br>make it a priority and call us<br>today for an appointment.</p>
      <p class="contact-label">Book An Appointment</p>
      <p class="contact-phone">(555) 014-2780</p>
      <p class="contact-email">info@evergreenmindhealth.com</p>
      <div class="contact-rule"></div>
      <p class="contact-address">1480 Maplecrest Drive, Suite 200<br>Riverton, CA 90000. <b>Fax:</b> (555) 014-2781</p>
    </section>

    <div class="divider"></div>

    <section class="benefits">
      <h2 class="benefits-title">We Listen, Care, and Help<br>You Live A BETTER Life</h2>
      <h3 class="benefits-sub">Why choose us?</h3>
      <ul class="benefits-list">
        <li>We are an integrative holistic psychiatric center.</li>
        <li>Our mission is to provide compassionate quality care.</li>
        <li>We provide psychiatric services including medication management and psychotherapy.</li>
        <li>We listen, care, and empower you to live better.</li>
        <li>We accept major insurances.</li>
      </ul>
    </section>

    <footer class="footer">Evergreen Mind Health and Wellness, APNC</footer>
  </main>
</body>
</html>
```